Flyer/Broschürre für Ambulanter Betreuungsdienst
Zielgruppe
Ambulanter Betreuungsdienst,Dienstleistungen für Senioren und Menschen mit Beeinträchtigung
Nach Paragraph 43b 45a/b & 53b SGBXI
Unterstützung im Alltag:
-Begleitung zu Arztbesuchen,Therapien &Terminbegleitung aller Art,
-Hilfe beim Einkaufen & Besorgungen + Transport
-Unterstützung bei der Tagesstrukturierung & Organisation im Alltag
-Erinnerungsservice zb. Einahme von Medikamenten ggbf. Kontrolle
-Begleitung zu Sportveranstaltungen,Theater uvm.
für zuverlässige Sicherheit und Orientierung.
-Gemeinsames Spazieren gehen ( Bewegungsangebote)
- Lesen & Vorlesen
-Gemeinsames Kochen und geselschaft leisten beim essen.
-Unterstützung bei Terminplanungen,Hilfe bei der komunikation mit Medizinischen Personal.
Soziale Betreuung & Aktivierung:
-Geselschaft leisten,Gespräche führen ;
-Freizeitaktivitäten Planen & Durchführen
-Gemeinsames Lesen und Vorlesen
-Karten & Brettspiele spielen
-Malen & Basteln
-Briefe schreiben,Emails verfassen
-Gemeinsam alte interessen wecken und neue finden.
-Angehörige entlasten
-kommunikation & Informationsaustausch über Fortschritte und Bedürfnisse
-Betreuung & Aktivierung für Menschen mit Demenz
-Erinnerungspflege,Biografie Arbeit
-Individuelle Betreuung
-Kurz und Langzeit Betreuung
-Nachtpflege
-Bewegungsangebote
-Spiele spielen zb. Brett & Gemeinschsftsspiele
Dienstleistungen Haushaltsbereich
-Reinigung von Böden(Saugen & Wischen)
-Reinigung Küche und Bad
-Bett frisch Beziehen
-Fenster Reinigung (innen & außen)
-Haustiere versorgen (mit dem Hund spazieren gehen)
-Wäsche waschen
-Dekorieren
-uvm
Aufgabenstellung
Freundliches Design , vertrauenswürdiges Erscheinungsbild mit warmen Farben.
Firmenname ( Sonnwerk) logo sollte einen Sonnwerk darstellen.
Slogan Text:
Verlässlichkeit und Fürsorge mit Herz & Verstand.
Format soll handlich und nicht zu klein sein,damit Senioren es gut lesen bzw erkennen können.

```html
<!DOCTYPE html>
<html lang="de">
<head>
<meta charset="utf-8">
<title>Sonnwerk – Leistungen</title>
<link rel="stylesheet" href="https://fonts.googleapis.com/css2?family=Poppins:wght@700;800&family=Varela+Round&display=swap">
<style>
  :root {
    --burgundy: #7f1338;
    --peach: #f5b09a;
    --white: #ffffff;
    --blush: #f6dadd;
    --blush-deep: #eec3c4;
  }
  * { margin: 0; padding: 0; box-sizing: border-box; }
  html, body { width: 1200px; height: 848px; overflow: hidden; background: var(--burgundy); }
  .flyer {
    position: relative; width: 1200px; height: 848px; overflow: hidden;
    background: var(--burgundy); color: var(--white);
    font-family: "Varela Round", "Nunito", sans-serif;
  }
  .photo { position: absolute; top: 0; height: 240px; }
  .photo--garden { left: 0; width: 404px; background: linear-gradient(135deg, #4f5a3e 0%, #b9b2a4 45%, #8a8d86 100%); }
  .photo--hands { left: 404px; width: 404px; background: linear-gradient(120deg, #7c9c92 0%, #c8b9a8 55%, #d9d0c4 100%); }
  .photo--park { left: 808px; width: 392px; background: linear-gradient(135deg, #2f4a22 0%, #6f8a4a 45%, #e8e2cf 100%); }
  .wave { position: absolute; top: 0; left: 0; width: 1200px; height: 300px; }
  .column { position: absolute; }
  .column--daily { left: 41px; top: 202px; width: 350px; }
  .column--social { left: 445px; top: 291px; width: 340px; }
  .column--dementia { left: 849px; top: 292px; width: 330px; }
  .column__title {
    font-family: "Poppins", sans-serif; font-weight: 800; font-size: 17.5px; line-height: 24px;
    padding-bottom: 6px; border-bottom: 1.5px solid var(--white); margin-bottom: 20px; letter-spacing: 0.1px;
  }
  .column--daily .column__title { width: 322px; }
  .column--social .column__title { width: 323px; }
  .column--dementia .column__title { width: 323px; margin-bottom: 28px; }
  .services { list-style: none; }
  .services li {
    position: relative; padding-left: 24px; font-size: 18.3px; line-height: 24px;
    margin-bottom: 8px; white-space: nowrap; letter-spacing: 0.2px;
  }
  .services li::before {
    content: ""; position: absolute; left: 1px; top: 7px; width: 11px; height: 11px;
    border-radius: 50%; background: var(--white);
  }
  .mascot-area {
    position: absolute; left: 823px; top: 664px; width: 365px; height: 184px;
    border-radius: 16px 16px 0 0;
    background: linear-gradient(160deg, var(--blush) 0%, var(--blush-deep) 100%);
  }
</style>
</head>
<body>
<main class="flyer">
  <div class="photo photo--garden" role="img" aria-label="Foto: lachende Seniorin mit Betreuerin im Garten"></div>
  <div class="photo photo--hands" role="img" aria-label="Foto: helfende Hände stützen eine ältere Person mit Gehstock"></div>
  <div class="photo photo--park" role="img" aria-label="Foto: Betreuerin mit Seniorin im Rollstuhl im Park"></div>

  <svg class="wave" viewBox="0 0 1200 300" aria-hidden="true">
    <path fill="var(--peach)" d="M0 112 C 250 140, 500 220, 800 232 C 1000 238, 1120 200, 1200 168 L1200 300 L0 300 Z"/>
    <path fill="var(--burgundy)" d="M0 120 C 250 155, 520 262, 790 268 C 990 272, 1120 230, 1200 209 L1200 300 L0 300 Z"/>
  </svg>

  <section class="column column--daily">
    <h2 class="column__title">Unterstützung im Alltag</h2>
    <ul class="services">
      <li>Begleitung zu Arztbesuchen,<br>Therapien und Terminbegleitung<br>aller Art</li>
      <li>Hilfe beim Einkaufen und<br>Besorgungen + Transport</li>
      <li>Unterstützung und Organisation bei<br>der Tagesstrukturierung / im Alltag</li>
      <li>Erinnerungsservice<br>(z.B. Medikamenteneinnahme<br>und ggbf. Kontrolle)</li>
      <li>Begleitung zu Veranstaltungen,<br>(Theater, Sport uvm.) für zuver-<br>lässige Sicherheit und Orientierung</li>
      <li>Bewegungsangebote (gemeinsam<br>Spazieren etc.)</li>
      <li>Gemeinsames Kochen und<br>Gesellschaft leisten beim essen</li>
      <li>Unterstützung bei Terminplanungen,<br>Hilfe bei Kommunikation mit<br>medizinischen Personal</li>
    </ul>
  </section>

  <section class="column column--social">
    <h2 class="column__title">Soziale Betreuung &amp; Aktivierung</h2>
    <ul class="services">
      <li>Gesellschaft leisten,<br>Gespräche führen</li>
      <li>Planung und Durchführung von<br>Freizeitaktivitäten</li>
      <li>Gemeinsames Lesen und Vorlesen</li>
      <li>Karten und Brettspiele spielen</li>
      <li>Malen und Basteln</li>
      <li>Verfassen von Briefen und Emails</li>
      <li>Gemeinsames Wecken und Finden<br>alter und neuer Interessen</li>
      <li>Entlastung Angehöriger</li>
      <li>Kommunikation und Informations-<br>austausch über Fortschritte<br>und Bedürfnisse</li>
    </ul>
  </section>

  <section class="column column--dementia">
    <h2 class="column__title">Betreuung und Aktivierung für<br>Menschen mit Demenz</h2>
    <ul class="services">
      <li>Erinnerungspflege,<br>Biografie-Arbeit</li>
      <li>Individuelle Betreuung</li>
      <li>Kurz- und Langzeitbetreuung</li>
      <li>Nachtpflege</li>
      <li>Bewegungsangebote</li>
      <li>Spiele spielen<br>(z.B. Brett &amp; Gemeinschaftsspiele)</li>
    </ul>
  </section>

  <div class="mascot-area" role="img" aria-label="Illustration: bunter Singvogel auf einem Ast mit Blättern und Blüten"></div>
</main>
</body>
</html>
```